Website Design for Bright Path Learning

The business is called Bright Path Learning - a Drug & Alcohol Education program for Sydney school kids. I wish to create a simple online business card which covers who we are, the programs we offer and why they should choose us. I would like the business page to be very colourful and school-friendly, but with the seriousness of alcohol and drug use. I have attached some pictures and logos for the business. The programs are called 'clear road' for high school, and 'step ahead' for primary school. The logo is black & white. There is also a photo of the manager with some kids.

```html
<!DOCTYPE html>
<html lang="en">
<head>
<meta charset="utf-8">
<title>Bright Path Learning</title>
<link rel="stylesheet" href="https://fonts.googleapis.com/css2?family=Open+Sans:wght@400;600;700&display=swap">
<style>
  :root {
    --ink: #2f2f2f;
    --body: #444;
    --muted: #8a8a8a;
    --lime: #a9c41a;
    --lime-light: #c3d94a;
    --lime-dark: #98b011;
    --link: #1b5fa8;
    --page: #fbfcfc;
    --footer: #e1e1e1;
    --dots: #c9c9c9;
    --fb: #3b5998;
    --tw: #2ba7e0;
    --li: #1a75b0;
  }
  * { box-sizing: border-box; margin: 0; padding: 0; }
  html, body { width: 1024px; height: 1200px; overflow: hidden; }
  body { background: var(--page); font-family: "Open Sans", Arial, sans-serif; color: var(--body); position: relative; }
  .wrap { position: absolute; left: 137px; width: 752px; }

  .site-header { position: absolute; top: 0; left: 0; width: 1024px; height: 74px; background: #fff; }
  .brand { top: 18px; font-size: 26px; font-weight: 700; color: #1e1e1e; display: flex; align-items: center; gap: 10px; letter-spacing: -0.5px; }
  .brand-mark { width: 16px; height: 16px; background: #1e1e1e; }
  .social { display: flex; gap: 7px; }
  .social span { width: 24px; height: 24px; border-radius: 50%; display: block; }
  .social .s1 { background: var(--fb); } .social .s2 { background: var(--tw); } .social .s3 { background: var(--li); }
  .header-social { position: absolute; top: 28px; right: 136px; gap: 5px; }
  .header-social span { width: 20px; height: 20px; }

  .main-nav { position: absolute; top: 74px; left: 0; width: 1024px; height: 42px; background: linear-gradient(var(--lime-light), var(--lime) 45%, var(--lime-dark)); border-bottom: 1px solid #8ea10e; }
  .main-nav ul { list-style: none; display: flex; position: absolute; left: 138px; top: 12px; gap: 32px; }
  .main-nav a { color: #fff; text-decoration: none; font-weight: 700; font-size: 13.5px; letter-spacing: .3px; }

  .hero { position: absolute; top: 116px; left: 0; width: 1024px; height: 378px; background: linear-gradient(100deg, #9c8478 0%, #c9b4a6 25%, #e9e1da 50%, #d8d4cf 75%, #bfbcb6 100%); }
  .hero-text { position: absolute; left: 137px; top: 240px; }
  .hero h1 { color: var(--lime-light); font-size: 29px; font-weight: 700; letter-spacing: .5px; }
  .hero p { color: #fff; font-size: 19px; line-height: 23px; margin-top: 12px; }

  .col { position: absolute; top: 536px; width: 238px; }
  .section-title { font-size: 19.5px; font-weight: 700; color: var(--ink); padding: 0 2px 14px; border-bottom: 3px dotted var(--dots); }
  .thumb { margin-top: 11px; height: 109px; background: #e8e8e8; border-radius: 3px; }
  .thumb.warm { background: linear-gradient(90deg, #e8e8e8, #c9806c 30%, #e6e2df 55%, #3f5a48 80%, #e8e8e8); }
  .thumb.icon-art { background: radial-gradient(ellipse at 50% 50%, #cfd6b8 0%, #e8e8e8 60%); }
  .col p, .welcome-text p { font-size: 10.4px; line-height: 14.4px; margin-top: 20px; }
  .read-more { display: inline-block; margin-top: 20px; color: var(--link); font-size: 10.5px; font-weight: 700; text-decoration: underline; }

  .welcome { position: absolute; top: 836px; left: 137px; width: 480px; }
  .welcome .section-title, .news .section-title { font-weight: 400; font-size: 20px; padding-bottom: 13px; }
  .welcome-photo { position: absolute; top: 53px; left: 1px; width: 238px; height: 167px; border-radius: 3px; background: linear-gradient(90deg, #cfcac4, #a99a8f 50%, #d4cfc9); }
  .welcome-text { position: absolute; top: 43px; left: 257px; width: 224px; }
  .welcome-text p { font-size: 10.2px; line-height: 15.2px; margin-top: 12px; }
  .welcome-text p + p { margin-top: 15px; }
  .welcome-text .read-more { margin-top: 17px; }

  .news { position: absolute; top: 836px; left: 649px; width: 239px; }
  .news .section-title { display: flex; align-items: center; gap: 8px; }
  .news-item { position: relative; height: 100px; margin-top: 8px; }
  .news-item h3 { font-size: 12.2px; font-weight: 600; color: var(--ink); padding-left: 1px; }
  .news-thumb { position: absolute; top: 20px; left: -2px; width: 68px; height: 58px; border-radius: 3px; background: linear-gradient(135deg, #eceae8, #c9a999 55%, #2c2f3f); }
  .news-body { position: absolute; top: 20px; left: 80px; width: 160px; font-size: 9.8px; line-height: 14.4px; color: var(--muted); }
  .news-date { display: flex; align-items: center; gap: 4px; margin-top: 4px; font-size: 7.6px; font-weight: 700; color: #777; }

  .site-footer { position: absolute; top: 1116px; left: 0; width: 1024px; height: 84px; background: var(--footer); }
  .footer-links { position: absolute; left: 138px; top: 28px; font-size: 10.4px; font-weight: 700; color: #3b4654; letter-spacing: .5px; word-spacing: 3px; }
  .copyright { position: absolute; left: 137px; top: 51px; font-size: 10.3px; color: #444; }
  .footer-social { position: absolute; left: 396px; top: 24px; gap: 11px; }
  .footer-social span { width: 21px; height: 21px; }
  .contact { position: absolute; left: 745px; top: 23px; font-size: 10.4px; color: #333; }
  .contact li { list-style: none; display: flex; align-items: center; gap: 14px; height: 24px; }
</style>
</head>
<body>
  <header class="site-header">
    <div class="wrap brand"><span class="brand-mark"></span>Bright Path</div>
    <div class="social header-social"><span class="s1"></span><span class="s2"></span><span class="s3"></span></div>
  </header>

  <nav class="main-nav">
    <ul>
      <li><a href="#">HOME</a></li>
      <li><a href="#">PROGRAMS</a></li>
      <li><a href="#">ABOUT</a></li>
      <li><a href="#">BLOG</a></li>
      <li><a href="#">CONTACT</a></li>
    </ul>
  </nav>

  <section class="hero" role="img" aria-label="Photo of the program manager crouching by a wall with a family of students">
    <div class="hero-text">
      <h1>Bright Path Learning</h1>
      <p>A Drug &amp; Alcohol Education program<br>for Sydney school kids</p>
    </div>
  </section>

  <section class="col" style="left:137px">
    <h2 class="section-title">ABOUT US</h2>
    <div class="thumb warm" role="img" aria-label="Photo of two school girls giving a high five"></div>
    <p>Lorem ipsum dolor sit amet, consectetur adipisicing elit, sed do eiusmod tempor incididunt ut labore et dolore magna aliqua. Ut enim ad minim veniam, quis nostrud exercitation.</p>
    <a class="read-more" href="#">READ MORE</a>
  </section>

  <section class="col" style="left:391px">
    <h2 class="section-title">CLEAR ROAD</h2>
    <div class="thumb icon-art" role="img" aria-label="Clear Road program artwork"></div>
    <p>Lorem ipsum dolor sit amet, consectetur adipisicing elit, sed do eiusmod tempor incididunt ut labore et dolore magna aliqua. Ut enim ad minim veniam, quis nostrud exercitation.</p>
    <a class="read-more" href="#">READ MORE</a>
  </section>

  <section class="col" style="left:649px">
    <h2 class="section-title">STEP AHEAD</h2>
    <div class="thumb icon-art" role="img" aria-label="Step Ahead program artwork"></div>
    <p>Lorem ipsum dolor sit amet, consectetur adipisicing elit, sed do eiusmod tempor incididunt ut labore et dolore magna aliqua. Ut enim ad minim veniam, quis nostrud exercitation.</p>
    <a class="read-more" href="#">READ MORE</a>
  </section>

  <section class="welcome">
    <h2 class="section-title">WELCOME TO OUR SITE</h2>
    <div class="welcome-photo" role="img" aria-label="Portrait photo of the program manager"></div>
    <div class="welcome-text">
      <p>Lorem ipsum dolor sit amet, consectetur adipisic-ing elit, sed do eiusmod tempor incididunt ut labore et dolore magna aliqua. Ut enim ad minim veniam, quis nostrud exercitation.</p>
      <p>Lorem ipsum dolor sit amet, consectetur adipisic-ing elit, sed do eiusmod tempor incididunt ut labore et dolore magna aliqua. Ut enim ad minim veniam, quis nostrud exercitation.</p>
      <a class="read-more" href="#">READ MORE</a>
    </div>
  </section>

  <aside class="news">
    <h2 class="section-title">
      <svg width="16" height="16" viewBox="0 0 16 16" aria-hidden="true"><rect x="1" y="3" width="14" height="12" fill="none" stroke="#777" stroke-width="1.5"/><rect x="1" y="3" width="14" height="3" fill="#777"/><rect x="4" y="1" width="2" height="4" fill="#777"/><rect x="10" y="1" width="2" height="4" fill="#777"/></svg>
      LATEST NEWS
    </h2>
    <article class="news-item">
      <h3>There are many variations of passages</h3>
      <div class="news-thumb" role="img" aria-label="Photo of two students in uniform"></div>
      <div class="news-body">The point of using Lorem Ipsum is that it has a more-or-less normal distribution of letters, as opposed..
        <div class="news-date"><svg width="8" height="8" viewBox="0 0 8 8" aria-hidden="true"><rect x=".5" y="1.5" width="7" height="6" fill="none" stroke="#888"/><rect x=".5" y="1.5" width="7" height="1.5" fill="#888"/></svg>8 December 2013</div>
      </div>
    </article>
    <article class="news-item">
      <h3>All the Lorem Ipsum generators</h3>
      <div class="news-thumb" role="img" aria-label="Photo of a smiling student"></div>
      <div class="news-body">The point of using Lorem Ipsum is that it has a more-or-less normal distribution of letters, as opposed..
        <div class="news-date"><svg width="8" height="8" viewBox="0 0 8 8" aria-hidden="true"><rect x=".5" y="1.5" width="7" height="6" fill="none" stroke="#888"/><rect x=".5" y="1.5" width="7" height="1.5" fill="#888"/></svg>8 December 2013</div>
      </div>
    </article>
  </aside>

  <footer class="site-footer">
    <div class="footer-links">LINKS &nbsp;| &nbsp;LINKS | &nbsp;LINKS | &nbsp;LINKS</div>
    <div class="copyright">Copyright © 2014 All rights reserved. &nbsp;Company Name</div>
    <div class="social footer-social"><span class="s1"></span><span class="s2"></span><span class="s3"></span></div>
    <ul class="contact">
      <li><svg width="16" height="12" viewBox="0 0 16 12" aria-hidden="true"><rect width="16" height="12" rx="1" fill="#777"/><path d="M1 1l7 6 7-6" fill="none" stroke="#e1e1e1" stroke-width="1.3"/></svg>hello@brightpathlearning.com.au</li>
      <li><svg width="16" height="14" viewBox="0 0 16 14" aria-hidden="true"><path d="M3 1l3 3-1.5 2c1 2 2.5 3.5 4.5 4.5L11 9l3 3-2 2C6 13 2 8 1 3z" fill="#777"/></svg>02-5550-1842</li>
    </ul>
  </footer>
</body>
</html>
```